Twin Ravens Sparkling

Hi all,

Thanks for taking the time to check out our brief.

Twin Ravens is an Australian wine company based in Victoria, and have been around for more than 20 years. We have a well-known sparkling Chardonnay Pinot Noir that needs a package revamp and we need your help!

Check out our current package here: http://www.twinravens.example.au/our-wines/dsp-default_b.cfm?loadref=17

So here's the brief:

1. Use of the Twin Ravens logo (silhouette) and text mandatory - but can be as small/large as required.

2. Design must be shown on a sparkling bottle.

3. Can be closed with cork or crown seal - neck label/hood not mandatory.

4. Front label size to be no larger than 75mm high x 100mm wide. Back label to be no larger than 75mm x 100mm

5. Label does not have to be square/rectangular. Happy to see thoughts outside the box.

6. Design cannot be printed onto the bottle - must be on a label that can be applied to the bottle.

7. Be forward thinking. Be interesting. This design does not have to tie into our still (red and white) wine range.

8. Mandatory information to be shown on front label - a. Wine of Australia - b. Sparkling Chardonnay Pinot Noir

9. Mandatory info for front label - a. 750mL - b. Alcohol e.g. 13.5% ALC/VOL - c. Wine of Australi - d. Producer address (please insert dummy address at this stage - e. standard drinks e.g. approx 8.0 standard drinks (this can also be shown in the standard drinks glass logo) - f. space for a tasting blurb

10. Try to stay away from anything floral or overly girly.

Requirements
Must have
• Design must be shown on a sparkling wine bottle & include the full label design separately
Should not have
• Try to stay away from anything too floral and overly girly.

```html
<!DOCTYPE html>
<html lang="en">
<head>
<meta charset="utf-8">
<title>Twin Ravens Sparkling – Front Label</title>
<link rel="stylesheet" href="https://fonts.googleapis.com/css2?family=Bodoni+Moda:ital,wght@1,400&family=Cinzel:wght@400&family=Pinyon+Script&family=Roboto:wght@300;400&family=Roboto+Condensed:wght@300&display=swap">
<style>
  :root {
    --page-bg: #eeeae3;
    --label-dark: #1c171d;
    --label-mid: #2b2530;
    --label-edge: #141015;
    --ink-light: #f2f0ee;
    --ink-soft: #c9c5c8;
    --ink-muted: #a9a4a8;
    --mark-tone: #5a5560;
    --hairline: rgba(242, 240, 238, 0.28);
  }
  * { margin: 0; padding: 0; box-sizing: border-box; }
  html, body {
    width: 1200px;
    height: 900px;
    overflow: hidden;
    background: var(--page-bg);
  }
  .canvas {
    position: relative;
    width: 1200px;
    height: 900px;
  }
  /* Front label: 100 mm wide × 75 mm high, drawn at 1040 × 780 px */
  .front-label {
    position: absolute;
    left: 80px;
    top: 60px;
    width: 1040px;
    height: 780px;
    border-radius: 50%;
    background: radial-gradient(ellipse at 50% 40%, var(--label-mid) 0%, var(--label-dark) 60%, var(--label-edge) 100%);
    box-shadow: 0 10px 30px rgba(0,0,0,0.18);
    color: var(--ink-light);
    text-align: center;
  }
  .front-label > * {
    position: absolute;
    left: 0;
    width: 100%;
  }
  .brand-mark {
    top: 62px;
    left: 485px;
    width: 70px;
    height: 70px;
    border-radius: 50%;
    background: var(--mark-tone);
    opacity: 0.55;
  }
  .brand-name {
    top: 148px;
    font-family: "Cinzel", serif;
    font-weight: 400;
    font-size: 22px;
    line-height: 1;
    letter-spacing: 0.32em;
    padding-left: 0.32em;
  }
  .brand-rule {
    top: 186px;
    left: 360px;
    width: 320px;
    height: 6px;
  }
  .wine-style {
    top: 206px;
    font-family: "Pinyon Script", cursive;
    font-size: 34px;
    line-height: 1.2;
    color: var(--ink-soft);
  }
  .wine-variety {
    top: 252px;
    font-family: "Bodoni Moda", serif;
    font-style: italic;
    font-weight: 400;
    font-size: 78px;
    line-height: 1;
  }
  .wine-origin {
    top: 352px;
    font-family: "Cinzel", serif;
    font-size: 15px;
    line-height: 1;
    letter-spacing: 0.16em;
    color: var(--ink-soft);
  }

  .label-details {
    top: 408px;
    left: 150px;
    width: 740px;
    height: 160px;
    display: grid;
    grid-template-columns: 200px 1fr 200px;
    column-gap: 30px;
    align-items: center;
  }
  .wine-strength {
    font-family: "Roboto", sans-serif;
    font-weight: 300;
    line-height: 1.15;
  }
  .strength-value { display: block; font-size: 32px; }
  .strength-unit { display: block; font-size: 22px; }
  .bottle-volume {
    display: block;
    margin-top: 12px;
    font-size: 20px;
    color: var(--ink-soft);
  }
  .tasting-space {
    height: 150px;
    border-top: 1px solid var(--hairline);
    border-bottom: 1px solid var(--hairline);
  }
  .standard-drinks {
    display: flex;
    flex-direction: column;
    align-items: center;
    gap: 8px;
    font-family: "Roboto", sans-serif;
    font-weight: 300;
    font-size: 13px;
    letter-spacing: 0.08em;
    line-height: 1.35;
    color: var(--ink-soft);
  }
  .drinks-glass { width: 54px; height: 64px; }
  .drinks-glass text {
    font-family: "Roboto", sans-serif;
    font-weight: 400;
    font-size: 15px;
    fill: var(--ink-light);
  }

  .producer {
    top: 598px;
    font-family: "Roboto", sans-serif;
    font-size: 14px;
    line-height: 1;
    letter-spacing: 0.08em;
    color: var(--ink-soft);
  }
  .producer-address {
    top: 624px;
    font-family: "Roboto Condensed", sans-serif;
    font-weight: 300;
    font-size: 13px;
    line-height: 1.4;
    color: var(--ink-muted);
  }
</style>
</head>
<body>
  <main class="canvas">
    <section class="front-label" aria-label="Twin Ravens sparkling front label">
      <div class="brand-mark" aria-hidden="true"></div>
      <h1 class="brand-name">TWIN RAVENS</h1>
      <svg class="brand-rule" viewBox="0 0 320 6" aria-hidden="true">
        <defs>
          <linearGradient id="ruleFade" x1="0" x2="1">
            <stop offset="0" stop-color="#ffffff" stop-opacity="0"/>
            <stop offset="0.5" stop-color="#ffffff" stop-opacity="1"/>
            <stop offset="1" stop-color="#ffffff" stop-opacity="0"/>
          </linearGradient>
        </defs>
        <path d="M0 3 Q160 0 320 3 Q160 6 0 3 Z" fill="url(#ruleFade)"/>
      </svg>
      <p class="wine-style">Sparkling Chardonnay</p>
      <h2 class="wine-variety">Pinot Noir</h2>
      <p class="wine-origin">WINE OF AUSTRALIA</p>

      <div class="label-details">
        <p class="wine-strength">
          <span class="strength-value">13.5%</span>
          <span class="strength-unit">ALC/VOL</span>
          <span class="bottle-volume">750mL</span>
        </p>
        <div class="tasting-space" role="img" aria-label="Space reserved for the tasting note"></div>
        <div class="standard-drinks">
          <svg class="drinks-glass" viewBox="0 0 54 64" aria-hidden="true">
            <path d="M8 4 H46 L40 60 H14 Z" fill="none" stroke="#c9c5c8" stroke-width="1.5"/>
            <text x="27" y="40" text-anchor="middle">8.0</text>
          </svg>
          <p>APPROX 8.0<br>STANDARD DRINKS</p>
        </div>
      </div>

      <p class="producer">PRODUCER</p>
      <p class="producer-address">The Twin Ravens Winery<br>3463 Harlow Lane, Avoca VIC</p>
    </section>
  </main>
</body>
</html>
```